Restaurant menu design

Design fine dinning menu for Indian restaurant. Restaurant location is on river side. So if design has some touch of Yarra river of Melbourne and Indian touch. It is not compulsory. Creative and modern design is required.
I want to print in A3 and folded take away sizes so design should for both.
1. In A3, backside we need to design drink menu. I am attaching our current restaurant menu for drinks name and price.

Target Market(s)

Indian / Australian Customer

Industry/Entity Type

Indian Food, Indian fine dining

Colors
F0912C
F2A743
F7CA91
FBE8D2
FDF5EE

Requirements
Must have
• Simple but district design
Should not have
• common other restaurant type menu. Too many colours.

```html
<!DOCTYPE html>
<html lang="en">
<head>
<meta charset="utf-8">
<title>Mira's Kitchen – Menu</title>
<link href="https://fonts.googleapis.com/css2?family=Hind:wght@400;600;700&display=swap" rel="stylesheet">
<style>
  :root{
    --page:#ebebeb;
    --paper:#ffffff;
    --ink:#1c1c1c;
    --muted:#333333;
    --green:#2d4a1f;
    --red:#b8172c;
    --red-deep:#8e1423;
    --wine:#7a1c23;
    --wine-dark:#54100f;
    --cream:#fdf5ee;
  }
  *{box-sizing:border-box;margin:0;padding:0}
  html,body{width:1029px;height:1200px;overflow:hidden}
  body{background:var(--page);font-family:"Hind",sans-serif;color:var(--ink);position:relative;
    font-variant-ligatures:none;font-feature-settings:"liga" 0,"clig" 0,"dlig" 0;}
  .sheet{position:absolute;left:135px;width:759px;height:537px;background:var(--paper);overflow:hidden}
  .sheet--outside{top:50px}
  .sheet--inside{top:614px}
  .sheet-art{position:absolute;inset:0;width:759px;height:537px}
  .block{position:absolute;width:215px}
  .heading{font-weight:700;font-size:10px;color:var(--green);margin-bottom:9px;line-height:1}
  .heading--light{color:#fff}
  .heading--dark{color:var(--ink)}
  .item{margin-bottom:9px;font-size:6.6px;line-height:8.4px}
  .item-head{display:flex;align-items:baseline;max-width:160px;font-weight:700}
  .item-head--wide{max-width:205px}
  .item-head--gap{max-width:178px}
  .item-name{white-space:nowrap}
  .leader{flex:1;border-bottom:1px dotted currentColor;margin:0 1px;transform:translateY(-2px)}
  .leader--blank{border-bottom:0}
  .item-price{white-space:nowrap}
  .item-desc{color:var(--muted);font-weight:400}
  .on-red .item,.on-red .item-desc{color:#fff}
  .brand{position:absolute;left:511px;top:222px;width:248px;text-align:center;
    font-weight:700;font-size:50px;line-height:46px;color:var(--red)}
  .item--tight{margin-bottom:6px}
</style>
</head>
<body>

<section class="sheet sheet--outside">
  <svg class="sheet-art" viewBox="0 0 759 537" aria-hidden="true">
    <path d="M251,392 C360,372 470,420 560,430 C650,440 710,410 759,380 L759,537 L251,537 Z" fill="var(--red)"/>
    <path d="M251,480 C380,450 520,500 640,470 C700,455 740,440 759,430 L759,537 L251,537 Z" fill="var(--red-deep)" opacity=".55"/>
  </svg>
  <svg class="sheet-art" viewBox="0 0 759 537" role="img" aria-label="Photo of golden samosas with green and red chutney bowls">
    <defs>
      <linearGradient id="samosaTone" x1="0" y1="0" x2="1" y2="1">
        <stop offset="0" stop-color="#c9a06a"/>
        <stop offset=".55" stop-color="#a9773e"/>
        <stop offset="1" stop-color="#6e4a2a"/>
      </linearGradient>
    </defs>
    <path d="M511,0 H759 V228 C690,192 600,185 511,200 Z" fill="url(#samosaTone)"/>
  </svg>

  <div class="block" style="left:17px;top:60px">
    <h2 class="heading">Non-Vegetarian Mains</h2>
    <div class="item"><div class="item-head"><span class="item-name">Raja Rani Chicken</span><span class="leader"></span><span class="item-price">$35</span></div><p class="item-desc">Char-grilled chicken tikka wrapped in a silky egg roll, layered with makhani sauce &amp; spinach gravy – regal flavours in every bite.</p></div>
    <div class="item"><div class="item-head"><span class="item-name">Butter Chicken</span><span class="leader"></span><span class="item-price">$29</span></div><p class="item-desc">A refined Delhi classic: chicken simmered in a tomato-butter sauce, smoky &amp; velvety.</p></div>
    <div class="item"><div class="item-head"><span class="item-name">Lamb Rogan Josh</span><span class="leader"></span><span class="item-price">$29</span></div><p class="item-desc">Kashmiri-style lamb curry, slow-braised in aromatic spices with a deep, rich flavour.</p></div>
    <div class="item"><div class="item-head"><span class="item-name">Dhaba Goat Masala</span><span class="leader"></span><span class="item-price">$29</span></div><p class="item-desc">A rustic North Indian goat curry, slow-cooked with onions, garlic, and earthy spices – inspired by India's iconic roadside kitchens.</p></div>
  </div>

  <div class="block" style="left:17px;top:270px">
    <h2 class="heading">Rice &amp; Biryanis</h2>
    <div class="item item--tight"><div class="item-head"><span class="item-name">Plain Basmati Rice</span><span class="leader"></span><span class="item-price">$8</span></div><p class="item-desc">Steamed long-grain basmati rice, light &amp; fluffy.</p></div>
    <div class="item item--tight"><div class="item-head"><span class="item-name">Jeera Rice</span><span class="leader"></span><span class="item-price">$8</span></div><p class="item-desc">Basmati rice tempered with roasted cumin seeds.</p></div>
    <div class="item item--tight"><div class="item-head"><span class="item-name">Lemon Coconut Rice</span><span class="leader"></span><span class="item-price">$10</span></div><p class="item-desc">Fragrant rice infused with lemon zest, curry leaves &amp; coconut.</p></div>
    <div class="item item--tight"><div class="item-head"><span class="item-name">Peas Pulao</span><span class="leader"></span><span class="item-price">$10</span></div><p class="item-desc">Delicate basmati rice cooked with sweet garden peas &amp; whole spices.</p></div>
    <div class="item item--tight"><div class="item-head"><span class="item-name">Biryani Flavoured Rice</span><span class="leader"></span><span class="item-price">$15</span></div><p class="item-desc">Aromatic saffron basmati rice prepared in biryani style.</p></div>
    <div class="item item--tight"><div class="item-head"><span class="item-name">Vegetable Dum Biryani</span><span class="leader"></span><span class="item-price">$28</span></div><p class="item-desc">Classic layered vegetable biryani with saffron, slow-cooked dum style.</p></div>
    <div class="item item--tight"><div class="item-head"><span class="item-name">Hyderabadi Chicken Biryani</span><span class="leader"></span><span class="item-price">$30</span></div><p class="item-desc">Fragrant rice layered with marinated chicken, spices &amp; saffron, served with raita.</p></div>
    <div class="item item--tight"><div class="item-head"><span class="item-name">Lamb Dum Biryani</span><span class="leader"></span><span class="item-price">$33</span></div><p class="item-desc">A celebratory lamb shank biryani, slow-cooked with caramelised onions, saffron &amp; spices – rich and aromatic.</p></div>
  </div>

  <div class="block" style="left:262px;top:22px">
    <h2 class="heading">Breads</h2>
    <div class="item item--tight"><div class="item-head"><span class="item-name">Classic Butter Naan</span><span class="leader"></span><span class="item-price">$6</span></div><p class="item-desc">Soft, fluffy tandoor-baked bread brushed with butter.</p></div>
    <div class="item item--tight"><div class="item-head"><span class="item-name">Garlic Naan</span><span class="leader"></span><span class="item-price">$7</span></div><p class="item-desc">Tandoor-baked naan with fresh garlic &amp; coriander.</p></div>
    <div class="item item--tight"><div class="item-head"><span class="item-name">Lachha Paratha</span><span class="leader"></span><span class="item-price">$8</span></div><p class="item-desc">Crisp, flaky, multi-layered paratha pan-fried with ghee.</p></div>
    <div class="item item--tight"><div class="item-head"><span class="item-name">Cheese Naan</span><span class="leader"></span><span class="item-price">$8</span></div><p class="item-desc">Stuffed with molten cheese, baked in the tandoor.</p></div>
    <div class="item item--tight"><div class="item-head"><span class="item-name">Cheese Garlic Naan</span><span class="leader"></span><span class="item-price">$8.50</span></div><p class="item-desc">Naan layered with garlic &amp; cheese — indulgent &amp; aromatic.</p></div>
  </div>

  <div class="block" style="left:262px;top:190px">
    <h2 class="heading">Sides</h2>
    <div class="item item--tight"><div class="item-head"><span class="item-name">Cucumber Raita</span><span class="leader"></span><span class="item-price">$6</span></div><p class="item-desc">Cool yogurt with cucumber, cumin &amp; mint.</p></div>
    <div class="item item--tight"><div class="item-head"><span class="item-name">Roasted Papadum</span><span class="leader"></span><span class="item-price">$4 (4 pcs)</span></div><p class="item-desc">Crispy lentil wafers roasted for a healthy crunch.</p></div>
    <div class="item item--tight"><div class="item-head"><span class="item-name">Masala Papad</span><span class="leader"></span><span class="item-price">$8 (2 pcs)</span></div><p class="item-desc">Papad topped with spiced onions, tomatoes &amp; herbs.</p></div>
    <div class="item item--tight"><div class="item-head"><span class="item-name">Onion Salad</span><span class="leader"></span><span class="item-price">$6</span></div><p class="item-desc">Fresh onion rings tossed with lime &amp; masala.</p></div>
    <div class="item item--tight"><div class="item-head"><span class="item-name">Garden Salad</span><span class="leader"></span><span class="item-price">$8</span></div><p class="item-desc">Seasonal greens dressed with lemon &amp; cumin.</p></div>
    <div class="item item--tight"><div class="item-head item-head--gap"><span class="item-name">Mango Chutney / Mint Chutney / Mixed Pickle</span><span class="leader leader--blank"></span><span class="item-price">$4</span></div><p class="item-desc">House-made condiments to complement your meal.</p></div>
  </div>

  <div class="block on-red" style="left:262px;top:411px">
    <h2 class="heading heading--light">Desserts</h2>
    <div class="item item--tight"><div class="item-head"><span class="item-name">Kunafa Nest Gulab Jamun with Rabri</span><span class="leader"></span><span class="item-price">$20</span></div><p class="item-desc">Golden kunafa nest cradling soft gulab jamun, draped in creamy rabri &amp; pistachios.</p></div>
    <div class="item item--tight"><div class="item-head"><span class="item-name">Mango Mousse Delight</span><span class="leader"></span><span class="item-price">$20</span></div><p class="item-desc">Alphonso mango mousse layered with coconut crumble &amp; fresh mint.</p></div>
    <div class="item item--tight"><div class="item-head"><span class="item-name">Kulfi Falooda Trio</span><span class="leader"></span><span class="item-price">$20</span></div><p class="item-desc">Traditional kulfi in pistachio, rose &amp; saffron, served with silky falooda.</p></div>
  </div>

  <p class="brand">Mira's<br>Kitchen</p>
</section>

<section class="sheet sheet--inside">
  <svg class="sheet-art" viewBox="0 0 759 537" role="img" aria-label="Darkened red-toned photo of grilled kebabs on a board with chillies and spices">
    <defs>
      <linearGradient id="kebabTone" x1="0" y1="0" x2="0" y2="1">
        <stop offset="0" stop-color="#9b2228"/>
        <stop offset=".45" stop-color="#7a1c23"/>
        <stop offset="1" stop-color="#4e0f12"/>
      </linearGradient>
    </defs>
    <rect x="251" y="0" width="260" height="537" fill="url(#kebabTone)"/>
  </svg>

  <div class="block" style="left:17px;top:26px">
    <h2 class="heading heading--dark">Vegetarian Entrées</h2>
    <div class="item"><div class="item-head"><span class="item-name">Classic Samosa</span><span class="leader"></span><span class="item-price">$16</span></div><p class="item-desc">Handcrafted pastry parcels filled with spiced potatoes &amp; peas, served with a duo of fresh mint-coriander chutney and sweet mango relish.</p></div>
    <div class="item"><div class="item-head"><span class="item-name">Crispy Onion &amp; Spinach Bhaji</span><span class="leader"></span><span class="item-price">$16</span></div><p class="item-desc">Crisp golden fritters of baby spinach &amp; onion, delicately spiced, paired with house chutneys.</p></div>
    <div class="item"><div class="item-head"><span class="item-name">Harabhara Edamame Kebab</span><span class="leader"></span><span class="item-price">$18</span></div><p class="item-desc">Pan-seared medallions of edamame and garden vegetables, stuffed with soft cheese and herbs, served with tangy yogurt dip.</p></div>
    <div class="item"><div class="item-head"><span class="item-name">Zafrani Paneer Tikka</span><span class="leader"></span><span class="item-price">$22</span></div><p class="item-desc">Cubes of cottage cheese marinated in saffron, cardamom &amp; smoky tandoor spices, grilled to perfection, served with mint chutney and microgreens.</p></div>
    <div class="item"><div class="item-head"><span class="item-name">Vada Pav Sliders</span><span class="leader"></span><span class="item-price">$16</span></div><p class="item-desc">A gourmet take on Mumbai's street legend: spiced potato croquette in a butter brioche bun, layered with tamarind, mint-coriander chutney &amp; fiery thecha, accompanied by crisp fried green chilli.</p></div>
  </div>

  <div class="block" style="left:17px;top:280px">
    <h2 class="heading">Non-Vegetarian Entrées</h2>
    <div class="item item--tight"><div class="item-head"><span class="item-name">Smoke Tandoori Chicken Tikka</span><span class="leader"></span><span class="item-price">$20</span></div><p class="item-desc">Charcoal-grilled chicken marinated overnight with aromatic spices, finished with a touch of smokey infusion.</p></div>
    <div class="item item--tight"><div class="item-head"><span class="item-name">Chicken Malai Tikka</span><span class="leader"></span><span class="item-price">$20</span></div><p class="item-desc">Tender chicken morsels marinated in cream, cheese &amp; cardamom, cooked gently in the tandoor for a melt-in-mouth experience.</p></div>
    <div class="item item--tight"><div class="item-head"><span class="item-name">Awadhi Fish Tikka</span><span class="leader"></span><span class="item-price">$22</span></div><p class="item-desc">Fresh barramundi fillets marinated with hand-pounded Awadhi spices, grilled for a delicate smoke flavour.</p></div>
    <div class="item item--tight"><div class="item-head"><span class="item-name">Tandoori Tiger Prawns</span><span class="leader"></span><span class="item-price">$24</span></div><p class="item-desc">Jumbo prawns infused with curry-leaf butter, garlic &amp; chilli, char-grilled for an indulgent coastal flavour.</p></div>
    <div class="item item--tight"><div class="item-head"><span class="item-name">Lamb Gilafi Seekh</span><span class="leader"></span><span class="item-price">$22</span></div><p class="item-desc">Minced lamb spiced with herbs, peppers &amp; aromatics, skewered &amp; flame-roasted, served with minted yogurt.</p></div>
    <div class="item item--tight"><div class="item-head"><span class="item-name">Tandoori Platter</span><span class="leader"></span><span class="item-price">$39</span></div><p class="item-desc">A chef's selection of smoky tandoori classics: Chicken Tikka, Malai Tikka, Lamb Seekh &amp; Awadhi Fish, presented with a medley of chutneys &amp; dips.</p></div>
  </div>

  <div class="block on-red" style="left:262px;top:26px">
    <h2 class="heading heading--light">Chaat</h2>
    <div class="item"><div class="item-head"><span class="item-name">Panipuri Experience</span><span class="leader"></span><span class="item-price">$20</span></div><p class="item-desc">Crisp puris filled with spiced potato, tangy chutneys &amp; chilled spiced water – a refined version of the street favourite.</p></div>
    <div class="item"><div class="item-head"><span class="item-name">Burrata Chaat</span><span class="leader"></span><span class="item-price">$20</span></div><p class="item-desc">Creamy burrata resting on crispy papdi, layered with tamarind glaze, mint chutney &amp; golden sev.</p></div>
    <div class="item"><div class="item-head"><span class="item-name">Deconstructed Samosa Chaat</span><span class="leader"></span><span class="item-price">$18</span></div><p class="item-desc">Crispy samosa pastry crumbles over spiced potato &amp; peas, dressed with chutneys, yogurt &amp; pomegranate jewels.</p></div>
  </div>

  <div class="block on-red" style="left:262px;top:290px">
    <h2 class="heading heading--light">Classic Curries</h2>
    <div class="item item--tight"><div class="item-head"><span class="item-name">Paneer / Kofta / Mixed Veg</span><span class="leader"></span><span class="item-price">$26</span></div><p class="item-desc">Choose your protein with a choice of gourmet curry bases.</p></div>
    <div class="item item--tight"><div class="item-head"><span class="item-name">Chicken / Lamb</span><span class="leader"></span><span class="item-price">$28</span></div><p class="item-desc">Choose your protein with a choice of gourmet curry bases.</p></div>
    <div class="item item--tight"><div class="item-head"><span class="item-name">Prawns / Fish</span><span class="leader"></span><span class="item-price">$30</span></div><p class="item-desc">Choose your protein with a choice of gourmet curry bases.</p></div>
    <div class="item item--tight"><div class="item-head"><span class="item-name">Vindaloo</span><span class="leader"></span></div><p class="item-desc">Fiery Goan-style curry with red chillies &amp; vinegar.</p></div>
    <div class="item item--tight"><div class="item-head"><span class="item-name">Saag</span><span class="leader"></span></div><p class="item-desc">Creamy buttered spinach slow-cooked with spices.</p></div>
    <div class="item item--tight"><div class="item-head"><span class="item-name">Korma</span><span class="leader"></span></div><p class="item-desc">Mild, creamy cashew &amp; saffron curry.</p></div>
    <div class="item item--tight"><div class="item-head"><span class="item-name">Masala</span><span class="leader"></span></div><p class="item-desc">Tomato &amp; onion base enriched with cream &amp; butter.</p></div>
    <div class="item item--tight"><div class="item-head"><span class="item-name">Madras</span><span class="leader"></span></div><p class="item-desc">Coconut-based curry with onions, garlic &amp; curry leaves.</p></div>
  </div>

  <div class="block" style="left:520px;top:26px">
    <h2 class="heading heading--dark">Indo-Chinese</h2>
    <div class="item"><div class="item-head"><span class="item-name">Vegetable Manchurian Dry</span><span class="leader"></span><span class="item-price">$22</span></div><p class="item-desc">Golden-fried vegetable dumplings wok-tossed in garlic, chilli &amp; soy glaze.</p></div>
    <div class="item"><div class="item-head"><span class="item-name">Paneer Chilli Dry</span><span class="leader"></span><span class="item-price">$24</span></div><p class="item-desc">Cottage cheese cubes tossed with peppers, onions &amp; chilli-garlic soy reduction.</p></div>
    <div class="item"><div class="item-head"><span class="item-name">Chilli Chicken Dry</span><span class="leader"></span><span class="item-price">$26</span></div><p class="item-desc">Tender chicken tossed with shallots, peppers &amp; fiery Indo-Chinese sauce.</p></div>
    <div class="item"><div class="item-head item-head--wide"><span class="item-name">Oriental Noodles</span><span class="leader"></span><span class="item-price">Veg $22 / Chicken $24</span></div><p class="item-desc">Stir-fried noodles with seasonal vegetables, wok-seared with soy &amp; garlic.</p></div>
  </div>

  <div class="block" style="left:520px;top:220px">
    <h2 class="heading heading--dark">Mira's Kitchen Special Vegetarian Curries</h2>
    <div class="item item--tight"><div class="item-head"><span class="item-name">Sham Savera Kofta</span><span class="leader"></span><span class="item-price">$26</span></div><p class="item-desc">Spinach dumplings filled with cottage cheese, simmered in a rich tomato-butter sauce – a true royal delicacy.</p></div>
    <div class="item item--tight"><div class="item-head"><span class="item-name">Mexican Salsa Paneer</span><span class="leader"></span><span class="item-price">$28</span></div><p class="item-desc">Paneer cubes tossed in a fusion of roasted Mexican-style tomato salsa and Indian spices – a bold East-meets-West creation.</p></div>
    <div class="item item--tight"><div class="item-head"><span class="item-name">Mushroom Mutter Masala</span><span class="leader"></span><span class="item-price">$28</span></div><p class="item-desc">Tender mushrooms and garden peas in a spiced onion-tomato gravy, finished with cream.</p></div>
    <div class="item item--tight"><div class="item-head"><span class="item-name">Kaju Curry</span><span class="leader"></span><span class="item-price">$28</span></div><p class="item-desc">A luxurious cashew-based curry enriched with aromatic spices, velvety texture &amp; buttery finish.</p></div>
    <div class="item item--tight"><div class="item-head"><span class="item-name">Cheese Butter Masala</span><span class="leader"></span><span class="item-price">$28</span></div><p class="item-desc">Paneer and soft cheese in a creamy, butter-rich tomato gravy – indulgent &amp; comforting.</p></div>
    <div class="item item--tight"><div class="item-head"><span class="item-name">Dal Tadka</span><span class="leader"></span><span class="item-price">$22</span></div><p class="item-desc">Yellow lentils tempered with garlic, cumin &amp; chilli, offering homestyle comfort with gourmet finesse.</p></div>
    <div class="item item--tight"><div class="item-head"><span class="item-name">Dal Makhani</span><span class="leader"></span><span class="item-price">$22</span></div><p class="item-desc">Black lentils, slow-cooked overnight with butter and cream – a timeless Delhi specialty.</p></div>
    <div class="item item--tight"><div class="item-head"><span class="item-name">Vegetable Dum Biryani</span><span class="leader"></span><span class="item-price">$28</span></div><p class="item-desc">Saffron-scented basmati rice layered with seasonal vegetables, sealed and slow-cooked in the dum style, served with cooling raita.</p></div>
  </div>
</section>

</body>
</html>
```